Hartwell Taproom Co Menu Design

I have an exisiting restaurant called Hartwell Taproom Co. We have an official logo and an existing menu. We need something more professional and vibrant. We are a great little brewpub and need our menu to reflect the same.
Updates

I have added our existing menu that has our logo on first page. Please use and insert menu items and pricing. Thank you for all your help! I really need a great look... also our web site is hartwelltaproomco.comĀ  that may help as well

I have been trying to uplaod pictures for the menu design today but for some reason I can not get them to upload on this site. Will keep trying and hope to have some posted soon.

I have submitted pictures to pixel harbor web administration and they will be posting to my project shortly.

All pictures have been posted for menu design. Thanks!

Industry/Entity Type

Restaurant

Requirements
Must have
• Great layout with pictures!!! Need it to be eye catching with current menu items and pricing. Needs to be a funtional format so I can easily changed to add or delete items as needed. I am looking for a one page menu that is 8 1/2 x 14 with front and back side print that will be placed in a clear menu cover.

```html
<!DOCTYPE html>
<html lang="en">
<head>
<meta charset="utf-8">
<title>Hartwell Taproom Co – Burgers &amp; Sandwiches</title>
<link rel="stylesheet" href="https://fonts.googleapis.com/css2?family=Titan+One&family=Arimo:ital,wght@0,400;0,700;1,700&display=swap">
<style>
  :root {
    --page-blue: #b9cce5;
    --frame-orange: #ea7a2a;
    --heading-orange: #f28a22;
    --heading-outline: #b8461a;
    --note-red: #e8131a;
    --ink: #151515;
    --photo-warm: #a8764a;
    --photo-green: #8a9a5a;
  }
  * { margin: 0; padding: 0; box-sizing: border-box; }
  html, body { width: 900px; height: 1200px; overflow: hidden; }
  body {
    background: #ffffff;
    font-family: "Arimo", Arial, sans-serif;
    color: var(--ink);
    position: relative;
  }
  .menu-page {
    position: absolute;
    inset: 0;
    background: var(--page-blue);
  }
  .frame-outer {
    position: absolute;
    left: 34px; top: 34px; right: 34px; bottom: 34px;
    border: 3px solid var(--frame-orange);
  }
  .frame-inner {
    position: absolute;
    left: 43px; top: 43px; right: 43px; bottom: 43px;
    border: 2px solid var(--frame-orange);
  }
  .section-title {
    position: absolute;
    left: 0; width: 900px;
    text-align: center;
    font-family: "Titan One", "Arial Black", sans-serif;
    font-size: 21px;
    letter-spacing: 0.5px;
    color: var(--heading-orange);
    -webkit-text-stroke: 0.6px var(--heading-outline);
    text-transform: uppercase;
  }
  .section-title.underlined { text-decoration: underline dotted var(--heading-outline) 1px; text-underline-offset: 3px; }
  .note {
    position: absolute;
    left: 50px; width: 800px;
    text-align: center;
    color: var(--note-red);
    font-weight: 700;
    font-style: italic;
    font-size: 13px;
    line-height: 18px;
  }
  .note.upright { font-style: normal; font-size: 13.5px; }
  .group-title {
    position: absolute;
    left: 55px;
    font-family: "Titan One", "Arial Black", sans-serif;
    font-size: 16px;
    color: var(--heading-orange);
    -webkit-text-stroke: 0.5px var(--heading-outline);
    text-transform: uppercase;
    white-space: nowrap;
  }
  .group-title .group-note {
    font-family: "Arimo", Arial, sans-serif;
    -webkit-text-stroke: 0;
    color: var(--note-red);
    font-style: italic;
    font-weight: 700;
    font-size: 13px;
    text-transform: none;
    margin-left: 4px;
  }
  .menu-item {
    position: absolute;
    left: 55px;
    width: 720px;
  }
  .item-name {
    font-weight: 700;
    font-size: 13.5px;
    line-height: 19px;
    text-transform: uppercase;
  }
  .item-line {
    font-weight: 700;
    font-size: 11.4px;
    line-height: 18px;
    letter-spacing: -0.1px;
    white-space: nowrap;
    position: relative;
  }
  .item-price {
    position: absolute;
    left: 586px;
    font-weight: 700;
    font-size: 11.6px;
  }
  .item-name-inline { font-size: 12.5px; text-transform: uppercase; }
  .food-photo {
    position: absolute;
    border-radius: 4px;
  }
  .photo-burger-fries {
    left: 710px; top: 294px; width: 156px; height: 114px;
    background: radial-gradient(circle at 35% 45%, #c98f58 0%, var(--photo-warm) 35%, #6e5a3c 70%, #d9b37a 100%);
  }
  .photo-salmon-burger {
    left: 727px; top: 722px; width: 137px; height: 106px;
    background: radial-gradient(ellipse at 50% 50%, #e4a063 0%, #c8773e 30%, var(--photo-green) 60%, #dfe4ea 100%);
  }
</style>
</head>
<body>
<main class="menu-page">
  <div class="frame-outer"></div>
  <div class="frame-inner"></div>

  <h1 class="section-title underlined" style="top:78px;">“The Burgers”</h1>
  <p class="note" style="top:118px;">All Angus and Chicken burgers are served on a French brioche bun and come with choice of regular fries or house side salad…<br>Sub Sweet potato fries $1.00 extra</p>

  <h2 class="group-title" style="top:176px;">Angus Burgers<span class="group-note">(1/2 lb 100% ANGUS&nbsp; BEEF!)</span></h2>

  <div class="menu-item" style="top:207px;">
    <div class="item-name">All American:</div>
    <div class="item-line">Served with all the fix’ins, Cheddar cheese, lettuce, tomato, onions and dressed with thousand island…<span class="item-price" style="left:586px;">$9.95</span></div>
  </div>

  <div class="menu-item" style="top:261px;">
    <div class="item-name">Bacon Bleu:</div>
    <div class="item-line">Topped with bleu cheese, bacon, grilled red onion, tomato, lettuce and dressed with bleu cheese dressing…<span class="item-price" style="left:583px;">$11.95</span></div>
  </div>

  <div class="menu-item" style="top:315px;">
    <div class="item-name">Mushroom Swiss:</div>
    <div class="item-line" style="margin-top:2px;">Topped with Swiss cheese, grilled onions, mushrooms, lettuce and tomato with mayo</div>
    <div class="item-line">(vegan option…all mushroom) …<span class="item-price" style="left:582px;">$10.95</span></div>
  </div>

  <div class="menu-item" style="top:391px;">
    <div class="item-name">Chipotle Angus:</div>
    <div class="item-line">Topped with aged provolone, avocado, bacon, lettuce, tomato and chipotle ranch. …<span class="item-price" style="left:586px;">$11.95</span></div>
  </div>

  <div class="menu-item" style="top:437px;">
    <div class="item-name">Californian:</div>
    <div class="item-line">Fire roasted green chili, pepper jack cheese, avocado, tomato, lettuce and chipotle ranch …<span class="item-price" style="left:586px;">$10.95</span></div>
  </div>

  <h2 class="group-title" style="top:492px;">Chicken Burgers<span class="group-note">&nbsp;(Full 8 ounce grilled mesquite chicken breast)</span></h2>

  <div class="menu-item" style="top:526px;">
    <div class="item-name">Chicken Bacon Ranch:</div>
    <div class="item-line">Grilled mesquite chicken breast, Apple wood smoked bacon, provolone cheese, lettuce and tomato,</div>
    <div class="item-line">then dressed with buttermilk ranch dressing …<span class="item-price" style="left:582px;">$10.95</span></div>
  </div>

  <div class="menu-item" style="top:594px;">
    <div class="item-name">Cali Chicken:</div>
    <div class="item-line">Grilled mesquite chicken breast, fire roasted green chili, Swiss cheese, avocado and tomato with</div>
    <div class="item-line">chipotle ranch dressing …<span class="item-price" style="left:582px;">$10.95</span></div>
  </div>

  <div class="food-photo photo-burger-fries" role="img" aria-label="Photo of an Angus bacon burger with a side of fries"></div>

  <h2 class="section-title" style="top:666px;">What the Tide Brought In</h2>
  <p class="note" style="top:692px;"><span style="font-style:normal;font-size:15px;">(</span>All seafood burgers are served with choice of sweet potato fries or side salad)</p>

  <div class="menu-item" style="top:734px;">
    <div class="item-line"><span class="item-name-inline">Salmon Bacon:</span> Wild Alaskan grilled salmon, apple wood smoked bacon, grilled onions, tomatoes,</div>
    <div class="item-line">mixed greens and chipotle ranch dressing&nbsp; on Hawaiian bun …<span class="item-price" style="left:586px;">$11.95</span></div>
  </div>

  <div class="menu-item" style="top:782px;">
    <div class="item-name">Lobster:</div>
    <div class="item-line">Succulent sweet grilled lobster is dressed with a Cajun slaw then topped with avocado and apple wood</div>
    <div class="item-line">smoked bacon on a French brioche bun…<span class="item-price" style="left:586px;">$12.95</span></div>
  </div>

  <div class="food-photo photo-salmon-burger" role="img" aria-label="Photo of a grilled salmon burger with greens on a Hawaiian bun"></div>

  <h2 class="section-title" style="top:864px;">Specialty Hot Sandwiches</h2>
  <p class="note upright" style="top:892px;"><span style="font-size:17px;">*</span>All our generous size grilled sandwiches come with choice of regular fries or side salad. Sub sweet potato fries for $1.00 extra only if not listed in order *Add avocado to any sandwich $0.95. Available bread choices are Baguette, Sourdough or Bavarian Rye.<br>Split any plate $2.00 extra… comes with full sides on each plate.</p>

  <div class="menu-item" style="top:963px;">
    <div class="item-name">BBQ Pulled Pork:</div>
    <div class="item-line">Piled high on Hawaiian bun drizzled with BBQ sauce and topped with apple cider slaw and sweet potato fries. …$9.95</div>
  </div>

  <div class="menu-item" style="top:1009px;">
    <div class="item-name">Pastrami and Swiss:</div>
    <div class="item-line">Deli style lean beef pastrami piled high with aged Swiss, sauerkraut and mustard on Bavarian rye bread …<span class="item-price" style="left:592px;">$9.95</span></div>
  </div>

  <div class="menu-item" style="top:1057px;">
    <div class="item-name">Chicken Caprese:</div>
    <div class="item-line">Our grilled mesquite chicken breast with tomato, basil pesto and provolone on a toasty baguette ...<span class="item-price" style="left:592px;">$8.95</span></div>
  </div>
</main>
</body>
</html>
```